Business Card for Dental Surgery

Professional and vibrant business card for dental surgery

Other side to incorporate space for appointment date and times

My website is www.tallowbydental.com.au

Target Market(s)

All

Industry/Entity Type

Dental

Requirements
Must have
• Catchy
Phone no, internet etc
Nice to have
• portray same image as website.
on reverse appointment side:
"Please give 24 hours notice if you cannot attend"
Nice colours

```html
<!DOCTYPE html>
<html lang="en">
<head>
<meta charset="utf-8">
<title>Tallowby Dental – Business Card</title>
<link rel="stylesheet" href="https://fonts.googleapis.com/css2?family=Arimo:ital,wght@0,400;0,700;1,400&display=swap">
<style>
  :root {
    --page-bg: #ffffff;
    --card-bg: #ffffff;
    --brand-purple: #8e2fd6;
    --brand-purple-fade: rgba(142, 47, 214, 0);
    --accent-lime: #a9ef3a;
    --header-grey: #646464;
    --text-dark: #111111;
    --text-grey: #4d5a5a;
    --shadow: rgba(0, 0, 0, 0.35);
  }
  * { margin: 0; padding: 0; box-sizing: border-box; }
  html, body {
    width: 1200px;
    height: 900px;
    overflow: hidden;
    background: var(--page-bg);
    font-family: "Arimo", Arial, sans-serif;
    color: var(--text-dark);
  }
  .canvas { position: relative; width: 1200px; height: 900px; }

  .side-label {
    position: absolute;
    left: 252px;
    font-size: 32px;
    color: var(--text-dark);
  }
  .side-label--front { top: 376px; }
  .side-label--back { top: 734px; }

  .card {
    position: absolute;
    left: 346px;
    width: 508px;
    background: var(--card-bg);
    box-shadow: 2px 3px 6px var(--shadow);
    overflow: hidden;
  }
  .card--front { top: 124px; height: 292px; }
  .card--back { top: 482px; height: 294px; }

  /* Front */
  .brand-name {
    position: absolute;
    right: 32px;
    top: 24px;
    font-size: 40px;
    font-weight: 700;
    letter-spacing: -1px;
    color: var(--brand-purple);
  }
  .dentist-name {
    position: absolute;
    right: 32px;
    top: 74px;
    font-size: 23px;
    font-weight: 700;
    color: var(--text-grey);
  }
  .accent-band {
    position: absolute;
    left: 0;
    top: 108px;
    width: 476px;
    height: 20px;
    background: linear-gradient(to right, var(--brand-purple) 0%, var(--brand-purple) 45%, var(--brand-purple-fade) 100%);
  }
  .address {
    position: absolute;
    left: 30px;
    top: 150px;
    font-size: 22px;
    line-height: 28px;
    color: var(--brand-purple);
  }
  .phone {
    position: absolute;
    right: 32px;
    top: 178px;
    font-size: 22px;
    color: var(--brand-purple);
  }
  .contact-band {
    position: absolute;
    left: 0;
    bottom: 0;
    width: 100%;
    height: 76px;
    background: var(--accent-lime);
    display: flex;
    flex-direction: column;
    justify-content: center;
    align-items: center;
    font-size: 21px;
    line-height: 25px;
    color: var(--text-dark);
  }

  /* Back */
  .appointment-header {
    height: 98px;
    background: var(--header-grey);
    border-bottom: 8px solid var(--accent-lime);
    display: flex;
    align-items: center;
    justify-content: center;
    font-size: 31px;
    color: #ffffff;
  }
  .appointment-fields { padding: 22px 0 0 50px; }
  .field {
    display: flex;
    align-items: flex-end;
    font-size: 32px;
    height: 40px;
    margin-bottom: 18px;
  }
  .field__line {
    margin-left: 10px;
    border-bottom: 2px solid var(--text-dark);
    margin-bottom: 4px;
  }
  .field__line--date { width: 320px; }
  .field__line--time { width: 320px; }
  .notice {
    position: absolute;
    left: 0;
    bottom: 22px;
    width: 100%;
    text-align: center;
    font-size: 19px;
    font-style: italic;
  }
</style>
</head>
<body>
<main class="canvas">
  <span class="side-label side-label--front">Front</span>
  <section class="card card--front" aria-label="Business card front">
    <div class="brand-name">Tallowby Dental</div>
    <div class="dentist-name">Dr Martin Hale BDS (Sydney)</div>
    <div class="accent-band" role="img" aria-label="Purple brushstroke accent band"></div>
    <div class="address">18 Carrow St.<br>Tallowby NSW 2290</div>
    <div class="phone">Phone: 02 9555 0142</div>
    <div class="contact-band">
      <span>Email: admin@tallowbydental.com.au</span>
      <span>www.tallowbydental.com.au</span>
    </div>
  </section>

  <span class="side-label side-label--back">Back</span>
  <section class="card card--back" aria-label="Business card back">
    <div class="appointment-header">Your Appointment</div>
    <div class="appointment-fields">
      <div class="field">Date:<span class="field__line field__line--date"></span></div>
      <div class="field">Time:<span class="field__line field__line--time"></span></div>
    </div>
    <p class="notice">Please give 24 hours notice if you cannot attend</p>
  </section>
</main>
</body>
</html>
```